Speisekarte für Pizzeria
Zielgruppe
Hallo in die Runde,
Wir würden gerne für unser Restaurant / Pizzeria eine neue Speisekarte haben.
Wir sind im höchsten Skigebiet Österreichs umgeben von Bergen und Schnee
am besten könnte ich es euch vorstellen bei einer Drohnen-Aufnahme die ihr unter folgendem Link sehen könnt:
www.firnblick.ag/panorama
Aufgabenstellung
Wir würden gerne ein quadratisches Format haben - 300x300mm
Der Druck sollte auf www.presswerk.at erfolgen
4 Umschlagseiten und 4 Kernseiten
Als Anhang hab ich euch meine jetzige Speisekarte drangehängt...diese ist lediglich im A4 Format und einfach eine klassische Speisekarte.
Nachtrag: weil da einige Fragen aufgekommen sind: die neue Karte sollte alle Speisen sowie auch alle Pizze und Getränke enthalten. Und auf der letzte Seite sollte irgendwie Werbung für unsere Appartments und unseren Wellness-Bereich gemacht werden. Foto gibt es unter www.almrosen.at ... wenn wir dann beim Finalisieren sind, kann ich die Fotos gerne in guter Qualität nachreichen
Wir haben bei uns im Haus auch Appartments mit Wellness Bereich und diese Gäste kommen natürlich auch ins Restaurnt. Weiters kommen aber natürlich auch Gäste aus anderen umliegenden Hotels / Betrieben...um diesen Gästen einen Anreiz zu schaffen, in Zukunft bei uns ihren Urlaub zu verbringen, würde ich gerne auf der letzten Seite unser Hotel bewerben...vielleicht mit einigen Fotos vom Schwimmbad / Ruheraum etc.
Wir haben hier auf dieser Plattform bereits einmal erfolgreich unsere Pizzakartons machen lassen... ein Foto von diesen habe ich auch drangehängt...aber das Design zu übernehmen ist kein Muss !
In unserer jetzigen Speisekarte sind nicht alle Spirituosen angeführt...dort sollte man vielleicht etwas mehr Platz einrechnen, damit ich alle Longdrinks etc. anführen kann. Dies würde ich dann aber erst gerne nachreichen wenn wir mal ein Design haben.

```html
<!DOCTYPE html>
<html lang="de">
<head>
<meta charset="utf-8">
<title>Berghof – Speisekarte</title>
<link href="https://fonts.googleapis.com/css2?family=Merriweather:wght@400;700&family=Playfair+Display:ital,wght@1,600&display=swap" rel="stylesheet">
<style>
:root{
  --brown:#5d4637;
  --brown-dark:#4a3629;
  --red:#e8474a;
  --gold:#f4c430;
  --ink:#3b2c22;
  --paper:#ffffff;
  --card:#f1f0ef;
  --leaf:#6fbf3a;
  --bg1:#8e8e8e;
  --bg2:#c9c9c9;
}
*{margin:0;padding:0;box-sizing:border-box}
html,body{width:1021px;height:1200px;overflow:hidden}
body{background:linear-gradient(180deg,var(--bg1),var(--bg2));font-family:"Merriweather",Georgia,serif;color:var(--ink);position:relative}
.page{position:absolute;width:264px;height:264px;background:var(--paper);box-shadow:0 2px 6px rgba(0,0,0,.35);overflow:hidden}
.page.framed::before{content:"";position:absolute;inset:6px;border:0.6px solid var(--brown);pointer-events:none;z-index:5}
.abs{position:absolute}
.photo{position:absolute;border-radius:8px}
.h-title{font-size:10.5px;color:var(--brown);font-weight:400}
.rule{border-bottom:0.7px solid var(--brown);padding-bottom:2px}
.item{margin-bottom:5px}
.item h4{font-size:5px;font-weight:700;color:var(--ink);line-height:1.2}
.item p{font-size:3.6px;line-height:1.3;color:#555}
.item .pr{font-size:3.6px;color:#555;margin-top:1px}
.row{display:flex;justify-content:space-between;align-items:baseline}
.light h4,.light p,.light .pr{color:#fff}
.leaf{display:inline-block;width:5px;height:3px;background:var(--leaf);border-radius:0 5px 0 5px;margin-left:2px;vertical-align:middle}
.script{font-family:"Playfair Display",Georgia,serif;font-style:italic;font-weight:600}
.dessert-list .item{margin-bottom:3.5px}
</style>
</head>
<body>

<!-- Cover -->
<section class="page framed" style="left:100px;top:52px">
  <div class="abs" style="left:0;right:0;top:78px;text-align:center;font-size:42px;color:var(--brown);letter-spacing:1px">BERGHOF</div>
  <div class="abs" style="left:0;right:0;top:155px;text-align:center;font-size:11px;line-height:1.3;color:var(--ink)">Toni's Team,<br>heisst Sie herzlich Willkommen<br>und wünscht Ihnen einen</div>
  <div class="abs script" style="left:54px;top:206px;width:156px;height:28px;background:var(--red);border-radius:3px;color:#fff;font-size:18px;text-align:center;line-height:28px">Guten Appetit !</div>
</section>

<!-- Favourites -->
<section class="page framed" style="left:378px;top:52px">
  <div class="abs" role="img" aria-label="Handschrift-Schriftzug Familien Rezept mit Herz" style="left:22px;top:14px;width:100px;height:62px;background:linear-gradient(135deg,#f3f3f3,#e6e6e6);border-radius:4px"></div>
  <div class="abs" style="left:0;top:82px;width:127px;height:37px;background:var(--red);border-radius:0 4px 4px 0;color:#fff;font-size:11px;line-height:1.1;padding:5px 0 0 18px">Die beliebtesten<br>Speisen von:</div>
  <div class="abs" style="left:139px;top:12px;width:114px;height:110px;background:var(--card);border-radius:8px;padding:8px">
    <div class="script" style="font-size:8.5px;color:var(--brown)">den Kindern Toni &amp; Felix</div>
    <div class="row" style="font-size:5px;font-weight:700;margin-top:2px"><span>Hausgemachtes Tiramisu</span><span style="font-weight:400">€ 9,90</span></div>
    <div style="font-size:3.4px;color:#666">- Das perfekte Dessert -</div>
    <div class="photo" role="img" aria-label="Stück Tiramisu auf weißem Teller" style="left:6px;top:36px;width:102px;height:68px;background:radial-gradient(ellipse at 50% 55%,#a87a4e,#e8dcc9 60%,#f1f0ef 80%)"></div>
  </div>
  <div class="abs" style="left:12px;top:128px;width:115px;height:124px;background:var(--card);border-radius:8px;padding:7px">
    <div class="script" style="font-size:9px;color:var(--brown)">Anna</div>
    <div class="row" style="font-size:5px;font-weight:700"><span>Carpaccio mit Trüffel-<br>Spaghettini</span><span style="font-weight:400">€ 29,90</span></div>
    <div style="font-size:3.4px;color:#666">ein original sizilianisches Rezept verfeinert mit Rucola &amp; Parmesan</div>
    <div class="photo" role="img" aria-label="Carpaccio mit Trüffel-Spaghettini und Rucola" style="left:5px;top:52px;width:105px;height:68px;background:radial-gradient(ellipse at 50% 60%,#b74c3d,#d9c3a6 55%,#eee 80%)"></div>
  </div>
  <div class="abs" style="left:139px;top:128px;width:114px;height:124px;background:var(--card);border-radius:8px;padding:7px">
    <div class="script" style="font-size:9px;color:var(--brown)">Lukas</div>
    <div class="row" style="font-size:5px;font-weight:700"><span>Sepp's Fischsuppe</span><span style="font-weight:400">€ 32,90</span></div>
    <div style="font-size:3.4px;color:#666">Tomaten-Safransuppe mit Karotten / Fenchel Sellerie / Zucchini, erlesene Fischfilets, Muscheln, Meeresfrüchten, Aioli dazu Knoblauchbrot</div>
    <div class="photo" role="img" aria-label="Schale Fischsuppe mit Garnelen und Kräutern" style="left:5px;top:56px;width:104px;height:64px;background:radial-gradient(ellipse at 50% 65%,#e9772f,#f3b58a 50%,#eee 80%)"></div>
  </div>
</section>

<!-- Starters, soups, salads -->
<section class="page framed" style="left:657px;top:52px">
  <div class="abs" style="left:15px;top:14px;width:117px;height:229px;background:var(--brown);border-radius:8px;padding:8px 8px">
    <div style="font-size:11px;color:var(--gold)" class="rule">Vorspeisen</div>
    <div class="light" style="margin-top:8px">
      <div class="item"><h4 style="font-weight:400">Carpaccio vom Tiroler Weiderind, Trüffelcreme, Parmesansplitter, hausgemachtes Brot</h4><div class="pr">€ 20,90</div></div>
      <div class="item"><h4 style="font-weight:400">Tartar von der Roten Beete &amp; Avocado mit Wakame Alge, Wasabi-Schaum und hausgemachtem Brot<span class="leaf"></span></h4><div class="pr">€ 16,90</div></div>
      <div class="item"><h4 style="font-weight:400">Vitello Tonnato rosa Kalbfleisch-Scheiben, Thunfischcreme, Rucola, Tomaten-Pesto, Kapern, hausgemachtes Brot</h4><div class="pr">€ 20,90</div></div>
    </div>
    <div class="photo" role="img" aria-label="Sandwich mit Roastbeef und Käse" style="left:0;right:0;bottom:0;height:95px;border-radius:0 0 8px 8px;background:linear-gradient(160deg,#a7653d,#7a3e2a 50%,#d6a23d)"></div>
  </div>
  <div class="abs" style="left:140px;top:14px;width:110px">
    <div class="h-title rule">Suppen</div>
    <div style="margin-top:6px">
      <div class="item"><h4>Tomatencremesuppe Basilikum / Croutons (auch vegan möglich)<span class="leaf"></span></h4><div class="pr">€ 7,20</div></div>
      <div class="item"><h4>Karamellisierte Zwiebelsuppe<span class="leaf"></span> im Tontopf serviert mit Käse-Crouton</h4><div class="pr">€ 7,50</div></div>
      <div class="item"><h4>Rindssuppe mit Kräuter-Frittaten</h4><div class="pr">€ 6,50</div></div>
    </div>
    <div class="h-title rule" style="margin-top:12px">Salate</div>
    <div style="margin-top:6px">
      <div class="item"><h4>gemischter Salat <span style="font-weight:400">€ 8,40</span><span class="leaf"></span></h4></div>
      <div class="item"><h4>Cesar Salat</h4><p>Das Original / Parmesansplitter /Croutons</p>
        <p>▸ <b>ohne Beilag</b><span class="leaf"></span> € 8,40</p>
        <p>▸ <b>mit gegrillter Hühnerbrust</b> € 23,90</p>
        <p>▸ <b>mit Knoblauch-Garnelen</b> € 29,90</p></div>
      <div class="item"><h4>Winter - Bowl<span class="leaf"></span></h4><p>Blattsalate / Granatapfelkerne / Schafskäse / Kirschtomaten Bulgur / Parmesanchips / Pinienkerne / rote Zwiebel / Gurken</p><div class="pr">€ 17,90</div></div>
    </div>
  </div>
</section>

<!-- Salad sides & pasta -->
<section class="page framed" style="left:100px;top:330px">
  <div class="abs" style="left:15px;top:15px;width:235px;height:106px;background:var(--red);border-radius:8px;padding:8px 10px">
    <div style="font-size:11px;color:#fff;line-height:1.1">Zu allen Salaten<br>empfehlen wir:</div>
    <div style="border-top:0.7px solid #fff;width:105px;margin:4px 0 5px"></div>
    <div class="light">
      <div class="item"><h4 style="font-weight:400">▸ Knoblauchbaguette mit<br>&nbsp;&nbsp;hausgemachtem Brot</h4><div class="pr">&nbsp;&nbsp;€ 6,50</div></div>
      <div class="item"><h4 style="font-weight:400">▸ Brotkorb</h4><div class="pr">&nbsp;&nbsp;€ 5,00</div></div>
      <div class="item"><h4 style="font-weight:400">▸ Pizzabrot</h4><div class="pr">&nbsp;&nbsp;€ 8,80</div></div>
    </div>
  </div>
  <div class="abs" role="img" aria-label="Geröstete Knoblauchbaguette-Scheiben mit Kräutern" style="left:108px;top:8px;width:150px;height:118px;border-radius:50%;background:radial-gradient(ellipse,#f1d27a,#d9a544 60%,rgba(217,165,68,0) 72%)"></div>
  <div class="abs" style="left:25px;top:133px;width:220px">
    <div class="h-title rule">Pasta / Fisch &amp; mehr</div>
  </div>
  <div class="abs" style="left:25px;top:155px;width:100px">
    <div class="item"><h4>Hausgemachte Schlutzkrapfen<span class="leaf"></span></h4><p>Teigtaschen gefüllt mit Topfen &amp; Spinat serviert mit Parmesan &amp; brauner Butter</p><p style="margin-top:2px">3 Stück € 14,50</p><p style="margin-top:2px">6 Stück € 26,90</p></div>
    <div class="item" style="margin-top:6px"><h4>Spaghetti al Chef</h4><p>Garnelen / Kirschtomaten / Zucchinistreifen / Knoblauch Kräuter / Olivenöl</p><div class="pr">€ 27,90</div></div>
    <div class="item" style="margin-top:6px"><h4>Spaghetti Bolognese</h4><div class="pr">€ 16,90</div></div>
  </div>
  <div class="abs" style="left:143px;top:157px;width:108px">
    <div class="item"><h4>Spaghetti Pesto<span class="leaf"></span></h4><p>Basilikum / Knoblauch / Olivenöl/ Pinienkerne / Parmesan</p><div class="pr">€ 16,50</div></div>
    <div class="item"><h4>Saiblingsfilet</h4><p>Kross gebraten aus Ötztaler Gewässern Tagliatelle / Fenchel / Lauch / Zitrone / Spinatblätter / Tomatenflocken</p><div class="pr">€ 31,20</div></div>
    <div class="item"><h4>Carpaccio mit Trüffel-Spaghettini</h4><p>ein original sizilianisches Rezept verfeinert mit Rucola &amp; Parmesan</p><div class="pr">€ 29,90</div></div>
  </div>
</section>

<!-- Grill -->
<section class="page framed" style="left:378px;top:330px">
  <div class="abs" style="left:17px;top:16px;width:115px">
    <div style="font-size:9.5px;color:var(--brown)">Aus dem Holzkohlegrill</div>
    <div style="font-size:6px;color:var(--brown)">bei offenem Feuer und 350°</div>
  </div>
  <div class="photo" role="img" aria-label="Steak auf dem Holzkohlegrill mit Flammen" style="left:132px;top:13px;width:119px;height:109px;background:radial-gradient(ellipse at 45% 60%,#7a3e22,#2a1a14 60%,#b34a1c)"></div>
  <div class="abs light" style="left:17px;top:48px;width:104px;height:66px;background:var(--red);border-radius:5px;padding:5px 8px">
    <div class="item" style="margin-bottom:3px"><h4 style="font-weight:400">Surf &amp; Turf</h4><p>200g heimisches Rinderfilet und Jumbo Garnelen</p><div class="pr">€ 49,90</div></div>
    <div class="item" style="margin-bottom:3px"><h4 style="font-weight:400">Filetsteak <span style="font-size:3.6px">ca. 250g</span></h4><div class="pr">€ 43,90</div></div>
    <div class="item"><h4 style="font-weight:400">Holzfällersteak</h4><p>vom Kräuterschwein Speck / Zwiebel / Pilze</p><div class="pr">€ 28,90</div></div>
  </div>
  <div class="abs" style="left:17px;top:128px;width:104px;height:23px;border:0.7px solid var(--red);border-radius:4px;padding:3px 5px">
    <div style="font-size:5px;color:var(--red)">Alle drei servieren wir mit</div>
    <div style="font-size:3.6px;color:#555">Gemüse / Pommes frites / 2 kalte Saucen / Kräuterbutter</div>
  </div>
  <div class="abs" style="left:17px;top:157px;width:110px">
    <div class="item"><h4>Tagliata</h4><p>ca. 250g vom Rumpsteak in Streifen geschnitten dazu Rucola Kirschtomaten / Parmesan / Knoblauchrot</p><div class="pr">€ 34,90</div></div>
  </div>
  <div class="abs" role="img" aria-label="Aufgeschnittenes Steak mit Rucola auf dunklem Teller" style="left:18px;top:188px;width:113px;height:70px;border-radius:50%;background:radial-gradient(ellipse,#8b3a2e,#3d2a22 60%,#222 70%)"></div>
  <div class="abs" style="left:132px;top:130px;width:119px;height:123px;background:var(--card);border-radius:8px;padding:6px 9px">
    <div style="font-size:6.5px;color:var(--brown);line-height:1.15;width:88px">Saftige hausgemachte Ripperl Sous vide gegart und im Grill verfeinert</div>
    <p style="font-size:3.8px;margin-top:3px;line-height:1.3;width:80px">am Brettl serviert / 2 Saucen / Folienkartoffel mit Dip und Knoblauchbaguette</p>
    <div class="pr" style="font-size:3.8px">€ 29,90</div>
    <div class="photo" role="img" aria-label="Glasierte Spareribs" style="left:10px;top:55px;width:110px;height:66px;background:linear-gradient(150deg,#c46a2a,#7c3118 60%,#f1f0ef 90%)"></div>
  </div>
  <div class="abs" style="left:229px;top:126px;width:27px;height:10px;background:#fff;border:0.8px solid var(--red);transform:rotate(22deg);color:var(--red);font-size:5px;font-weight:700;text-align:center;line-height:9px">TIPP!</div>
</section>

<!-- Main courses -->
<section class="page framed" style="left:657px;top:330px">
  <div class="abs" style="left:17px;right:17px;top:15px;text-align:center">
    <div class="h-title rule">Hauptspeisen</div>
  </div>
  <div class="abs" style="left:18px;top:40px;width:105px">
    <div class="item"><h4>Wiener Schnitzel vom Schwein mit Pommes frites und Preiselbeeren oder mit</h4><p>200g heimisches Rinderfilet und Jumbo Garnelen</p><div class="pr">€ 19,90</div></div>
    <div class="item"><h4>Schlössl Burger</h4><p>ca. 100g Rindfleisch mit Cheddarkäse gratiniert, Bacon, Gurken, rote Zwiebel, Tomaten, Salat, zweierlei Sauce und Pommes frites</p><div class="pr">€ 16,50</div></div>
    <div class="item"><h4>Stollenburger</h4><p>200g Rindfleisch (2 Patties) mit Cheddarkäse gratiniert, Bacon, Gurken, Salat, Zwiebel-Marmelade, Tomaten, Spiegelei zweierlei Saucen &amp; Pommes Frites</p><div class="pr">€ 20,90</div></div>
  </div>
  <div class="abs" style="left:138px;top:40px;width:108px">
    <div class="item"><h4>Veganer Burger<span class="leaf"></span></h4><p>Veganes Patty / Tomate / Salat / rote Zwiebel / Wakame Alge Limetten-Aioli und Pommes frites</p><div class="pr">€ 19,50</div></div>
    <div class="item"><h4>Sepp's Fischsuppeklare</h4><p>Tomaten-Safransuppe mit Gemüse, verschiedenen Fischfilets, Muscheln, Meeresfrüchten, Aioli - dazu Knoblauchbrot</p><div class="pr">€ 32,90</div></div>
    <div class="item"><h4>Garnelen im Tontopf</h4><p>250g Black Tiger Garnelen / Knoblauch / Kräuter / bestes Olivenöl hausgemachtes Aioli &amp; Brot zum Dippen</p><div class="pr">€ 28,50</div></div>
  </div>
  <div class="photo" role="img" aria-label="Eintöpfe in schwarzen Schalen mit Reis, Chili und Gewürzen" style="left:17px;top:163px;width:231px;height:86px;background:linear-gradient(100deg,#3a2a20,#c7651f 40%,#e6a030 60%,#8a1e14)"></div>
</section>

<!-- Pizza 1 -->
<section class="page framed" style="left:100px;top:607px">
  <div class="abs" style="left:19px;top:15px;width:105px">
    <div class="h-title rule">Unsere Pizze</div>
  </div>
  <div class="abs" style="left:19px;top:39px;width:105px">
    <div class="item" style="margin-bottom:3px"><div class="row"><h4>Margherita</h4><span class="pr">€ 11,90</span></div><p>Tomatensauce, Mozzarella, Basilikum, Olivenöl</p></div>
    <div class="item" style="margin-bottom:3px"><div class="row"><h4>Salami</h4><span class="pr">€ 14,50</span></div><p>Tomatensauce, Mozzarella, Salami, Parmesan, Olivenöl</p></div>
    <div class="item" style="margin-bottom:3px"><div class="row"><h4>Funghi</h4><span class="pr">€ 14,50</span></div><p>Tomatensauce, Mozzarella, Basilikum, Olivenöl</p></div>
    <div class="item" style="margin-bottom:3px"><div class="row"><h4>Prosciutto</h4><span class="pr">€ 14,50</span></div><p>Tomatensauce, Mozzarella, Schinken, Basilikum, Olivenöl</p></div>
    <div class="item" style="margin-bottom:3px"><div class="row"><h4>Prosciutto e Funghi</h4><span class="pr">€ 14,50</span></div><p>Tomatensauce, Mozzarella, frische Champignon, Schinken, Olivenöl</p></div>
    <div class="item" style="margin-bottom:3px"><div class="row"><h4>Prosciutto e Salami</h4><span class="pr">€ 14,50</span></div><p>Tomatensauce, Mozzarella, Salami, Schinken, Olivenöl</p></div>
    <div class="item" style="margin-bottom:3px"><div class="row"><h4>Tonno</h4><span class="pr">€ 14,90</span></div><p>Tomatensauce, Mozzarella, Thunfisch, Oregano, Olivenöl</p></div>
    <div class="item" style="margin-bottom:3px"><div class="row"><h4>Tonno e Cipolla</h4><span class="pr">€ 14,90</span></div><p>Tomatensauce, Mozzarella, Thunfisch, Zwiebel, Oregano, Olivenöl</p></div>
    <div class="item" style="margin-bottom:3px"><div class="row"><h4>Napoli</h4><span class="pr">€ 14,90</span></div><p>Tomatensauce, Mozzarella, Sardellen, Kapern, Oregano, Olivenöl</p></div>
  </div>
  <div class="abs" role="img" aria-label="Pizza Margherita" style="left:134px;top:14px;width:115px;height:68px;border-radius:50%;background:radial-gradient(ellipse,#d8452c,#e8b06a 65%,#c58a4c 72%,rgba(255,255,255,0) 74%)"></div>
  <div class="abs" role="img" aria-label="Pizza Hawaii mit Ananas" style="left:20px;top:180px;width:100px;height:75px;border-radius:50%;background:radial-gradient(ellipse,#f2c34d,#e7952f 55%,#c6793c 70%,rgba(255,255,255,0) 72%)"></div>
  <div class="abs" style="left:140px;top:80px;width:106px">
    <div class="item" style="margin-bottom:3px"><div class="row"><h4>Hawaii</h4><span class="pr">€ 14,90</span></div><p>Tomatensauce, Mozzarella, Schinken, frische Ananas, Basilikum, Olivenöl</p></div>
    <div class="item" style="margin-bottom:3px"><div class="row"><h4>Capricciosa</h4><span class="pr">€ 15,50</span></div><p>Tomatensauce, Mozzarella, Schinken Artischocken,frische Champignon, Basilikum, Olivenöl</p></div>
    <div class="item" style="margin-bottom:3px"><div class="row"><h4>Quattro Stagioni</h4><span class="pr">€ 15,50</span></div><p>Tomatensauce, Mozzarella, Schinken,frische Champignon, Artischocken, Oliven, Basilikum, Olivenöl</p></div>
    <div class="item" style="margin-bottom:3px"><div class="row"><h4>Diavola</h4><span class="pr">€ 15,50</span></div><p>Tomatensauce, Mozzarella, scharfe Salami,Nduja, Pfefferoni, Knoblauch</p></div>
    <div class="item" style="margin-bottom:3px"><div class="row"><h4>La Piccante</h4><span class="pr">€ 15,50</span></div><p>Tomatensauce, Mozzarella,scharfe Salami, Nduja, Pfefferoni, Peperonata, Zwiebel</p></div>
    <div class="item" style="margin-bottom:3px"><div class="row"><h4>Primavera</h4><span class="pr">€ 14,50</span></div><p>Tomatensauce, Mozzarella, Rucola, frische Tomaten, Frischkäse, Basilikum, Olivenöl</p></div>
    <div class="item" style="margin-bottom:3px"><div class="row"><h4>Vegetariana</h4><span class="pr">€ 14,50</span></div><p>Tomatensauce, Mozzarella, Mais, Artischocken, Rucola,frische Tomaten, Basilikum, Olivenöl</p></div>
    <div class="item" style="margin-bottom:3px"><div class="row"><h4>Rustica</h4><span class="pr">€ 15,90</span></div><p>Tomatensauce, Mozzarella, Tiroler Bauchspeck,Schinken, Mais, Zwiebel, Knoblauch</p></div>
    <div class="item" style="margin-bottom:3px"><div class="row"><h4>Carne e Pesce</h4><span class="pr">€ 15,50</span></div><p>Tomatensauce, Mozzarella,scharfe Salami, Thunfisch, Zwiebel, Basilikum, Olivenöl</p></div>
  </div>
</section>

<!-- Pizza 2 & kids -->
<section class="page framed" style="left:378px;top:607px">
  <div class="abs" style="left:19px;top:14px;width:105px">
    <div class="item" style="margin-bottom:3px"><div class="row"><h4>D.O.C.</h4><span class="pr">€ 16,5</span></div><p>Tomatensauce, Mozzarella,Rohschinken, Rucola, frische Tomaten,Parmesanspäne, Basilikum, Olivenöl</p></div>
    <div class="item" style="margin-bottom:3px"><div class="row"><h4>Crudo</h4><span class="pr">€ 16,5</span></div><p>Tomatensauce, Mozzarella, Rohschinken, Frischkäse, Parmesanspäne, Basilikum, Olivenöl</p></div>
    <div class="item" style="margin-bottom:3px"><div class="row"><h4>Siziliana</h4><span class="pr">€ 15,5</span></div><p>Tomatensauce, Mozzarella, Thunfisch, Sardellen, Oliven Zwiebel, Oregano, Olivenöl</p></div>
    <div class="item" style="margin-bottom:3px"><div class="row"><h4>Quattro formaggio</h4><span class="pr">€ 16,5</span></div><p>Tomatensauce, Mozzarella, Gorgonzolaund noch 3 weitere Käse-Sorten</p></div>
    <div class="item" style="margin-bottom:3px"><div class="row"><h4>La Bomba</h4><span class="pr">€ 15,9</span></div><p>Tomatensauce, Mozzarella, scharfe Salami, Gorgonzola</p></div>
    <div class="item" style="margin-bottom:3px"><div class="row"><h4>Frutti di Mare</h4><span class="pr">€ 19,9</span></div><p>Tomatensauce, Mozzarella, Tintenfisch, Miesmuscheln, Venusmuscheln, Garnelen, Greenshell-Muscheln, Knoblauch</p></div>
    <div class="item" style="margin-bottom:3px"><div class="row"><h4>Al Chef</h4><span class="pr">€ 19,9</span></div><p>Tomatensauce, Mozzarella, Garnelen &amp; Knoblauch</p></div>
  </div>
  <div class="abs" role="img" aria-label="Pizza mit Tomaten, Feta und Basilikum" style="left:132px;top:20px;width:118px;height:118px;border-radius:50%;background:radial-gradient(circle,#e4e0d6,#d8453a 45%,#d89a52 65%,rgba(255,255,255,0) 70%)"></div>
  <div class="abs" style="left:15px;top:148px;width:234px;height:101px;background:var(--brown);border-radius:8px">
    <div class="abs" role="img" aria-label="Kinderpizza auf Holzbrett" style="left:8px;top:-8px;width:95px;height:105px;border-radius:50%;background:radial-gradient(circle,#f3c35e,#e49a3c 50%,#b98350 66%,rgba(93,70,55,0) 70%)"></div>
    <div class="abs" style="left:122px;top:7px;width:105px">
      <div style="font-size:14px;font-weight:700;color:var(--gold);letter-spacing:.5px">KIDS</div>
      <div style="border-top:0.6px solid #c9b9aa;margin:3px 0 4px"></div>
      <div class="light">
        <div class="row" style="font-size:4.6px;color:#fff;font-weight:700;margin-bottom:3px"><span>Kinder-Pizza - FELIX - Margherita</span><span style="font-weight:400">€ 8,50</span></div>
        <div class="row" style="font-size:4.6px;color:#fff;font-weight:700;margin-bottom:3px"><span>Kinder-Pizza - EMIL - mit Schinken</span><span style="font-weight:400">€ 9,50</span></div>
        <div class="row" style="font-size:4.6px;color:#fff;font-weight:700;margin-bottom:3px"><span>Kinder-Pizza - TONI - mit Salami</span><span style="font-weight:400">€ 9,50</span></div>
        <p style="font-size:3.2px;color:#e8ddd3">Zusätzliche Beläge 0,80 - 3,50 | Halb/Halb Belegung ist leider nicht möglich!</p>
        <p style="font-size:3.2px;color:#e8ddd3;margin-top:3px">Aufgrund der verschiedenen Küchenbereiche ist es nicht immer möglich, normale Gerichte und Pizze gleichzeitig zu servieren.</p>
        <p style="font-size:4.4px;color:var(--gold);margin-top:4px">Vielen Dank für Ihr Verständnis!</p>
      </div>
    </div>
  </div>
</section>

<!-- Kids recommendations -->
<section class="page framed" style="left:657px;top:607px">
  <div class="abs" style="left:18px;right:18px;top:15px;text-align:center">
    <div class="h-title rule">Toni &amp; Felix empfehlen</div>
  </div>
  <div class="abs" role="img" aria-label="Comicfigur Feuerwehrmann" style="left:15px;top:38px;width:38px;height:48px;border-radius:6px;background:linear-gradient(#f2d14a,#2f4aa0)"></div>
  <div class="abs" role="img" aria-label="Comicfigur Burger" style="left:212px;top:38px;width:40px;height:48px;border-radius:6px;background:linear-gradient(#e6a048,#7a3a20)"></div>
  <div class="abs" role="img" aria-label="Comicfigur Huhn" style="left:13px;top:90px;width:40px;height:48px;border-radius:6px;background:linear-gradient(#f4d03a,#e87a2a)"></div>
  <div class="abs" role="img" aria-label="Comicfigur Katze mit Pasta" style="left:212px;top:92px;width:40px;height:46px;border-radius:6px;background:linear-gradient(#f6c34a,#e35a2c)"></div>
  <div class="abs" role="img" aria-label="Rotes Comicmonster" style="left:13px;top:140px;width:40px;height:50px;border-radius:6px;background:linear-gradient(#e8473a,#9c1f1c)"></div>
  <div class="abs" role="img" aria-label="Comicfigur Pommes-Tüte" style="left:210px;top:140px;width:44px;height:48px;border-radius:6px;background:linear-gradient(#f6d23a,#d43a2a)"></div>
  <div class="abs" role="img" aria-label="Comicräuber beim Rodeln" style="left:13px;top:192px;width:42px;height:50px;border-radius:6px;background:linear-gradient(#4d7ec8,#cf3a35)"></div>
  <div class="abs" role="img" aria-label="Limonadendosen in bunten Sorten" style="left:165px;top:215px;width:95px;height:46px;border-radius:6px;background:linear-gradient(100deg,#f1913a,#f4d33a 40%,#4fa6e0 60%,#e86fa0)"></div>

  <div class="abs" style="left:57px;top:39px;width:75px;height:40px;background:var(--brown);border-radius:5px;padding:4px 5px">
    <div style="font-size:5.6px;color:var(--gold)">Feuerwehrteller „Flo“</div><p style="font-size:4px;color:#fff;margin-top:2px">Schnitzel mit Pommes</p><p style="font-size:4px;color:#fff;margin-top:2px">€ 9,90</p></div>
  <div class="abs" style="left:135px;top:39px;width:75px;height:40px;background:var(--brown);border-radius:5px;padding:4px 5px">
    <div style="font-size:5.6px;color:var(--gold)">Kinder Burger</div><p style="font-size:4px;color:#fff">Burger Patty vom Rind mit Cheddarkäse Salatblatt &amp; Pomme</p><p style="font-size:4px;color:#fff">€ 11,50</p></div>
  <div class="abs" style="left:57px;top:88px;width:75px;height:40px;background:var(--brown);border-radius:5px;padding:4px 5px">
    <div style="font-size:5.6px;color:var(--gold)">Chicken Sticks</div><p style="font-size:4px;color:#fff">mit Pommes</p><p style="font-size:4px;color:#fff;margin-top:2px">€ 9,90</p></div>
  <div class="abs" style="left:135px;top:88px;width:75px;height:40px;background:var(--brown);border-radius:5px;padding:4px 5px">
    <div style="font-size:5.6px;color:var(--gold)">Katerteller</div><p style="font-size:4px;color:#fff">Mundgerechte Pasta mit Sauce Bolognese</p><p style="font-size:4px;color:#fff;margin-top:2px">€ 9,50</p></div>
  <div class="abs" style="left:57px;top:136px;width:75px;height:40px;background:var(--brown);border-radius:5px;padding:4px 5px">
    <div style="font-size:5.6px;color:var(--gold)">Rotes Monster</div><p style="font-size:4px;color:#fff">Mundgerechte Pasta mit Tomatensauce</p><p style="font-size:4px;color:#fff;margin-top:2px">€ 8,50</p></div>
  <div class="abs" style="left:135px;top:136px;width:75px;height:40px;background:var(--brown);border-radius:5px;padding:4px 5px">
    <div style="font-size:5.6px;color:var(--gold)">Pommes Män</div><p style="font-size:4px;color:#fff">Portion Pommes mit Ketchup &amp; Mayo</p><p style="font-size:4px;color:#fff;margin-top:2px">€ 6,90</p></div>
  <div class="abs" style="left:57px;top:185px;width:75px;height:40px;background:var(--brown);border-radius:5px;padding:4px 5px">
    <div style="font-size:5.6px;color:var(--gold)">Räuberteller</div><p style="font-size:4px;color:#fff">Leerer Teller zum Mitnaschen</p><p style="font-size:4px;color:#fff;margin-top:2px">€ 0,00</p></div>
  <div class="abs" style="left:135px;top:185px;width:60px;height:40px;background:var(--brown);border-radius:5px;padding:4px 5px">
    <div style="font-size:5.4px;color:var(--gold);line-height:1.1">..und dazu eine Gipfelquell Limo</div><p style="font-size:3.8px;color:#fff">Bubble Gum / Lemon / Peach</p><p style="font-size:3.8px;color:#fff">€ 4,30</p></div>
</section>

<!-- Dessert -->
<section class="page framed" style="left:240px;top:884px">
  <div class="abs" style="left:40px;right:25px;top:15px;text-align:center">
    <div class="h-title rule">Dessert</div>
  </div>
  <div class="abs" role="img" aria-label="Zitroneneis in Schale und Eiswaffeln mit Schoko- und Erdbeereis" style="left:112px;top:148px;width:152px;height:116px;border-radius:50% 0 0 0;background:radial-gradient(ellipse at 35% 55%,#f4ec9a,#f0c9cf 40%,#6b3f25 65%,rgba(255,255,255,0) 82%)"></div>
  <div class="abs dessert-list" style="left:24px;top:38px;width:84px">
    <div class="item"><h4>Wein-Nudeln</h4><p>Gebackene Grieß-Nudel in warmem Glühwein dazu leckeres Bratapfel-Eis</p><div class="pr">€ 9,90</div></div>
    <div class="item"><h4>Helles &amp; dunkles Schokoladenmousse</h4><p>it Himbeersauce &amp; Salz-Karamell-Eis</p><div class="pr">€ 9,90</div></div>
    <div class="item"><h4>Kokosnuss-Eis</h4><p>in der Schale serviert 8,90 Softeis Vanille / Erdbeere / Sternenmix</p><div class="pr">€ 3,20</div></div>
    <div class="item"><h4>Creme Brûlée</h4><p>Kirsch-Crumble &amp; Sauerrahm-Eis</p><div class="pr">€ 9,90</div></div>
    <div class="item"><h4>Hausgemachtes Tiramisu</h4><p>italienische Köstlichkeit</p><div class="pr">€ 9,90</div></div>
    <div class="item"><h4>Schatzkiste</h4><p>Vanille, Schokolade In der Schatztruhe mit Spielzeug</p><div class="pr">€ 5,50</div></div>
    <div class="item"><h4>Zitronensorbet</h4><p>in der Schale serviert</p><div class="pr">€ 8,90</div></div>
    <div class="item"><h4>Helles &amp; dunkles Schokoladenmousse</h4><p>it Himbeersauce &amp; Salz-Karamell-Eis</p><div class="pr">€ 9,90</div></div>
  </div>
  <div class="abs" style="left:140px;top:38px;width:100px">
    <div class="item" style="margin-bottom:8px"><h4>Heiße Liebe</h4><p>Cremiges Vanilleeis mit heißen Himbeeren und Sahne</p><div class="pr">€ 8,50</div></div>
    <div class="item" style="margin-bottom:8px"><h4>Coupe Danmark</h4><p>Vanilleeis mit heißer Schokosauce und Sahne</p><div class="pr">€ 8,50</div></div>
    <div class="item" style="margin-bottom:8px"><h4>Kindereisbecher mit Schokolinsen</h4><p>Vanille- und Erdbeereis, Sahne und einer kleinen Überraschung</p><div class="pr">€ 9,90</div></div>
    <div class="item"><h4>Softeis</h4><p>Vanille / Erdbeere / Sternenmix</p><div class="pr">€ 3,20</div></div>
  </div>
  <div class="abs" style="left:112px;top:247px;width:70px;height:12px;background:var(--red);border-radius:4px 0 0 0;color:#fff;font-size:5px;line-height:12px;text-align:center">Alle Preise inkl. MwSt.</div>
</section>

<!-- Hotel -->
<section class="page" style="left:518px;top:884px">
  <div class="abs" role="img" aria-label="Apart-Hotel im verschneiten Bergtal mit Nadelwald" style="left:0;top:0;width:264px;height:264px;background:linear-gradient(180deg,#7fa9d6 0%,#e8eef5 28%,#2f4a3a 48%,#dce4ec 68%,#8a6a55 82%,#2b2b2b 100%)"></div>
  <div class="abs" style="left:62px;top:28px;width:76px;text-align:center;font-size:13px;color:#fff">BERGHOF</div>
  <div class="abs" style="left:142px;top:0;width:122px;height:48px;background:var(--red);padding:6px 8px;color:#fff">
    <div class="script" style="font-size:12px">APART-HOTEL</div>
    <p style="font-size:5px;line-height:1.2">Ihr zweites Zuhause direkt an der PisteKomfortabel • Ideal für Familien Wellness der Extraklasse</p>
  </div>
  <div class="abs" role="img" aria-label="Restaurant-Innenraum" style="left:24px;top:194px;width:56px;height:56px;border-radius:50%;border:2px solid #fff;background:radial-gradient(circle,#c99a6a,#4a3428)"></div>
  <div class="abs" role="img" aria-label="Hallenbad mit blauer Beleuchtung" style="left:98px;top:194px;width:56px;height:56px;border-radius:50%;border:2px solid #fff;background:radial-gradient(circle,#9fd0f4,#1c4f9a)"></div>
  <div class="abs" role="img" aria-label="Ruheraum mit Holzmöbeln" style="left:172px;top:194px;width:56px;height:56px;border-radius:50%;border:2px solid #fff;background:radial-gradient(circle,#b98a5c,#3a2a22)"></div>
</section>

</body>
</html>
```